New business card design needed for Diesel Fitting (Mechanical) Company

We need a new business card for our company called "Gumtree Engine Works" that showcases our logo and business details.
Target Market(s)
Owners of all makes and models of vehicles, trucks, plant and machinery.
Industry/Entity Type
Mechanical
Contact Information for Business Card
The business card details need to include the following: Owners/Directors: Doug & Marisol Brent-Coyle ABN: 41 917 302 846 Address: 317 Wattlebrook Street REDGUM FLATS QLD 4899 Postal Address: PO Box 5791 REDGUM FLATS QLD 4899 Website: www.gewservice.com.au Phone: 4712 9083 Mobile: 0438 175 906 Emails: sales@gewservice.com.au; admin@gewservice.com.au; accounts@gewservice.com.au; parts@gewservice.com.au; office@gewservice.com.au, reception@gewservice.com.au
Look and feel

```html
<!DOCTYPE html>
<html lang="en">
<head>
<meta charset="utf-8">
<title>Gumtree Engine Works – Business Card</title>
<link rel="stylesheet" href="https://fonts.googleapis.com/css2?family=Arimo:wght@400;700&family=Roboto+Condensed:wght@700&display=swap">
<style>
  :root {
    --page-bg: #e2e2e2;
    --card-dark: #0d0d0d;
    --card-mid: #262626;
    --red: #e3212b;
    --orange: #f07a22;
    --yellow: #f5b21a;
    --white: #ffffff;
    --divider: rgba(255,255,255,0.35);
  }
  * { margin: 0; padding: 0; box-sizing: border-box; }
  html, body { width: 1200px; height: 1200px; overflow: hidden; }
  body {
    background: var(--page-bg);
    font-family: "Arimo", Arial, sans-serif;
    position: relative;
  }
  .card {
    position: absolute;
    left: 180px;
    width: 840px;
    height: 480px;
    border-radius: 30px;
    background: radial-gradient(ellipse at 50% 15%, var(--card-mid) 0%, #161616 45%, var(--card-dark) 100%);
    color: var(--white);
    overflow: hidden;
  }
  .card--front { top: 100px; }
  .card--back { top: 620px; }

  /* front */
  .owner {
    position: absolute;
    right: 450px;
    top: 180px;
    text-align: right;
    white-space: nowrap;
  }
  .owner__name {
    font-family: "Roboto Condensed", "Arial Narrow", sans-serif;
    font-weight: 700;
    font-size: 27px;
    color: var(--red);
    line-height: 1.1;
  }
  .owner__role {
    font-size: 19px;
    color: var(--orange);
    margin-top: 4px;
  }
  .owner__abn {
    font-size: 19px;
    color: var(--yellow);
    margin-top: 3px;
  }
  .divider {
    position: absolute;
    left: 421px;
    top: 105px;
    width: 1px;
    height: 235px;
    background: linear-gradient(to bottom, transparent, var(--divider) 20%, var(--divider) 80%, transparent);
  }
  .contact-list {
    position: absolute;
    left: 450px;
    top: 115px;
    list-style: none;
  }
  .contact-list li {
    display: flex;
    align-items: center;
    height: 23.6px;
    font-size: 19px;
    white-space: nowrap;
  }
  .icon {
    width: 16px;
    height: 16px;
    margin-right: 10px;
    flex: none;
    fill: var(--orange);
  }
  .address {
    position: absolute;
    left: 0;
    right: 0;
    top: 385px;
    text-align: center;
    font-size: 19px;
    line-height: 24px;
  }
  .address .icon { display: inline-block; vertical-align: -2px; margin-right: 4px; }

  /* back */
  .brand {
    position: absolute;
    left: 0;
    right: 0;
    top: 185px;
    display: flex;
    justify-content: center;
    align-items: center;
    gap: 18px;
  }
  .brand__mark {
    width: 54px;
    height: 54px;
    border-radius: 50%;
    background: var(--orange);
  }
  .brand__name {
    font-size: 44px;
    font-weight: 700;
    color: var(--white);
  }
  .website {
    position: absolute;
    left: 0;
    right: 0;
    top: 403px;
    text-align: center;
    font-size: 24px;
    letter-spacing: 7px;
    text-transform: uppercase;
  }
</style>
</head>
<body>

<section class="card card--front">
  <div class="owner">
    <p class="owner__name">Doug &amp; Marisol Brent-Coyle</p>
    <p class="owner__role">Owners/Directors</p>
    <p class="owner__abn">ABN: 41 917 302 846</p>
  </div>

  <div class="divider"></div>

  <ul class="contact-list">
    <li><svg class="icon" viewBox="0 0 16 16"><path d="M3.6 1.5l2.3 2.6-1.3 1.8c.9 2 2.5 3.6 4.5 4.5l1.8-1.3 2.6 2.3-1.4 2.2C7.2 13.3 2.7 8.8 1.4 3z"/></svg>4712 9083</li>
    <li><svg class="icon" viewBox="0 0 16 16"><path d="M4.5 1h7v14h-7zM5.7 2.3v10h4.6v-10zM7.3 13h1.4v1H7.3z" fill-rule="evenodd"/></svg>0438 175 906</li>
    <li><svg class="icon" viewBox="0 0 16 16"><path d="M1.5 4h13v9h-13zM2.5 5l5.5 4 5.5-4z" fill-rule="evenodd"/></svg>sales@gewservice.com.au</li>
    <li><svg class="icon" viewBox="0 0 16 16"><path d="M1.5 4h13v9h-13zM2.5 5l5.5 4 5.5-4z" fill-rule="evenodd"/></svg>admin@gewservice.com.au</li>
    <li><svg class="icon" viewBox="0 0 16 16"><path d="M1.5 4h13v9h-13zM2.5 5l5.5 4 5.5-4z" fill-rule="evenodd"/></svg>accounts@gewservice.com.au</li>
    <li><svg class="icon" viewBox="0 0 16 16"><path d="M1.5 4h13v9h-13zM2.5 5l5.5 4 5.5-4z" fill-rule="evenodd"/></svg>parts@gewservice.com.au</li>
    <li><svg class="icon" viewBox="0 0 16 16"><path d="M1.5 4h13v9h-13zM2.5 5l5.5 4 5.5-4z" fill-rule="evenodd"/></svg>office@gewservice.com.au</li>
    <li><svg class="icon" viewBox="0 0 16 16"><path d="M1.5 4h13v9h-13zM2.5 5l5.5 4 5.5-4z" fill-rule="evenodd"/></svg>reception@gewservice.com.au</li>
    <li><svg class="icon" viewBox="0 0 16 16"><circle cx="8" cy="8" r="6.5"/><path d="M4 5.5c1.5.3 2 1.3 1.6 2.5 1.2.4 1.3 1.7.7 2.7M10 3c-.4 1.3.3 2 1.5 2.2.2 1.3-.5 2.4-1.7 2.3" stroke="#1a1a1a" stroke-width="1.2" fill="none"/></svg>gewservice.com.au</li>
  </ul>

  <div class="address">
    <p><svg class="icon" viewBox="0 0 16 16"><path d="M8 1a5 5 0 0 1 5 5c0 3.5-5 9-5 9S3 9.5 3 6a5 5 0 0 1 5-5zm0 2.8a2.2 2.2 0 1 0 0 4.4 2.2 2.2 0 0 0 0-4.4z" fill-rule="evenodd"/></svg>317 Wattlebrook Street Redgum Flats Qld 4899</p>
    <p><svg class="icon" viewBox="0 0 16 16"><path d="M8 1a5 5 0 0 1 5 5c0 3.5-5 9-5 9S3 9.5 3 6a5 5 0 0 1 5-5zm0 2.8a2.2 2.2 0 1 0 0 4.4 2.2 2.2 0 0 0 0-4.4z" fill-rule="evenodd"/></svg>PO Box 5791 Redgum Flats Qld 4899</p>
  </div>
</section>

<section class="card card--back">
  <div class="brand">
    <span class="brand__mark"></span>
    <span class="brand__name">Gumtree Engine Works</span>
  </div>
  <p class="website">www.gewservice.com.au</p>
</section>

</body>
</html>
```